VaultMeridan Business Card Re-Design

VaultMeridan is a specialized information security company that applies its proven methodology of security Assessment, Development, Integration and Training (A-D-I-T) to provide cyber security services in the areas of Data Protection, Network Defense and Compliance. We need the current business card re-designed to properly scale the fonts and possibly rearranging some elements (icons, lettering, etc.) to make the card more appealing to the eye. The card should have the logo that is on the web site (www.vaultmeridan-example.com). We would like ideas for both a black card (black background) and a white card (white background). We prefer rounded corners to help the card stand out but are open to all ideas. FYI: VaultMeridan's slogan is "...your security is our business".

Target Market(s)

#1 US Government Contracting Companies, #2 Commercial Companies, #3 Gen. Public.

Industry/Entity Type

Business

Contact Information for Business Card

See Description; open to the use of different fonts.

Font styles to use
Sans Serif

Colors
000000
ec1f27
ffffff

Requirements
Must have
• Company logo on web site, rounded corners, list of company offerings on the back of the card.
Nice to have
• Icons
Should not have
• none

```html
<!DOCTYPE html>
<html lang="en">
<head>
<meta charset="utf-8">
<title>VaultMeridan Business Cards</title>
<link href="https://fonts.googleapis.com/css2?family=Lato:wght@400;700;900&display=swap" rel="stylesheet">
<style>
  :root {
    --red: #ec1f27;
    --black: #141414;
    --card-black: #1c1c1c;
    --white: #ffffff;
    --paper: #f4f4f4;
    --ink: #3a3a3a;
    --muted: #7a7a7a;
    --stage: #2a2a2a;
    --map-light: #ececec;
    --map-dark: #242424;
  }
  * { box-sizing: border-box; margin: 0; padding: 0; }
  html, body { width: 1200px; height: 873px; overflow: hidden; }
  body {
    background: var(--stage);
    font-family: "Lato", sans-serif;
    position: relative;
  }
  .card {
    position: absolute;
    width: 540px;
    height: 309px;
    border-radius: 18px;
    overflow: hidden;
  }

  /* Front (white) */
  .card-front {
    left: 60px; top: 110px;
    background: linear-gradient(160deg, var(--white) 0%, var(--paper) 100%);
  }
  .front-map {
    position: absolute; left: 40px; top: 96px; width: 300px; height: 160px;
    border-radius: 6px;
    background: var(--map-light);
    opacity: .6;
  }
  .front-brand {
    position: absolute; left: 36px; top: 52px;
  }
  .brand-name {
    display: flex; align-items: center; gap: 9px;
    font-weight: 900; font-size: 28px; letter-spacing: 1.5px; color: var(--ink);
    white-space: nowrap;
  }
  .brand-mark { width: 14px; height: 14px; background: var(--red); flex: none; }
  .brand-tagline {
    margin-top: 4px; margin-left: 24px;
    font-size: 10.5px; letter-spacing: 2.4px; text-transform: uppercase; color: var(--muted);
    white-space: nowrap;
  }
  .front-person {
    position: absolute; left: 40px; top: 178px;
  }
  .person-name { font-weight: 900; font-size: 21px; color: var(--red); white-space: nowrap; }
  .person-creds { font-size: 10.5px; color: var(--muted); margin-left: 6px; font-weight: 400; }
  .person-title { font-weight: 700; font-size: 12.5px; color: var(--ink); margin-top: 3px; margin-left: 112px; }
  .front-divider {
    position: absolute; left: 272px; top: 56px; width: 2px; height: 120px;
    background: linear-gradient(to bottom, transparent, #9a9a9a, transparent);
  }
  .contact-list {
    position: absolute; left: 288px; top: 60px; list-style: none;
  }
  .contact-list li {
    display: flex; align-items: center; gap: 8px;
    font-size: 11.5px; color: var(--ink); height: 26px; white-space: nowrap;
  }
  .contact-list svg { width: 13px; height: 13px; flex: none; }
  .front-band {
    position: absolute; left: 0; right: 0; bottom: 0; height: 34px;
    background: var(--red); color: var(--white);
    font-weight: 700; font-size: 13px; letter-spacing: .3px;
    display: flex; align-items: center; justify-content: center;
  }

  /* Back (black) */
  .card-back {
    left: 600px; top: 440px;
    background: linear-gradient(160deg, #262626 0%, var(--card-black) 60%, var(--black) 100%);
    color: var(--white);
    text-align: center;
  }
  .back-map {
    position: absolute; left: 90px; top: 95px; width: 360px; height: 150px;
    border-radius: 6px;
    background: var(--map-dark);
    opacity: .7;
  }
  .back-brand {
    position: relative; margin-top: 38px;
    display: flex; justify-content: center; align-items: center; gap: 10px;
    font-weight: 900; font-size: 36px; letter-spacing: 2px; color: var(--white);
  }
  .offerings {
    position: relative; margin-top: 22px; list-style: none;
    font-size: 11.5px; font-weight: 700; line-height: 19px; color: #e6e6e6;
    white-space: nowrap;
  }
  .sep { color: var(--red); margin: 0 6px; font-weight: 900; }
  .back-web {
    position: relative; margin-top: 10px;
    display: flex; align-items: center; justify-content: center; gap: 10px;
    font-weight: 700; font-size: 12px; letter-spacing: 3px; color: var(--red);
  }
  .back-web .rule { width: 80px; height: 1px; background: #bdbdbd; }
</style>
</head>
<body>

<section class="card card-front" aria-label="Business card front">
  <div class="front-map" role="img" aria-label="Faint dotted world map background"></div>
  <div class="front-brand">
    <div class="brand-name"><span class="brand-mark"></span>VaultMeridan</div>
    <div class="brand-tagline">Information Security</div>
  </div>
  <div class="front-person">
    <div class="person-name">Dana Whitford<span class="person-creds">CISSP, CEH</span></div>
    <div class="person-title">President CEO</div>
  </div>
  <div class="front-divider"></div>
  <ul class="contact-list">
    <li>
      <svg viewBox="0 0 16 16"><path fill="#ec1f27" d="M3 1h3l1 4-2 1c1 2 3 4 5 5l1-2 4 1v3c0 1-1 2-2 2C7 15 1 9 1 3c0-1 1-2 2-2z"/></svg>
      240 555 0148
    </li>
    <li>
      <svg viewBox="0 0 16 16"><rect x="2" y="2" width="12" height="12" fill="none" stroke="#7a7a7a" stroke-width="1.6"/></svg>
      301 555 0193
    </li>
    <li>
      <svg viewBox="0 0 16 16"><rect x="1" y="3" width="14" height="10" fill="#ec1f27"/><path d="M1 3l7 6 7-6" fill="none" stroke="#fff" stroke-width="1.3"/></svg>
      info@vaultmeridan-example.com
    </li>
    <li>
      <svg viewBox="0 0 16 16"><rect x="1" y="3" width="14" height="10" fill="#ec1f27"/><path d="M1 3l7 6 7-6" fill="none" stroke="#fff" stroke-width="1.3"/></svg>
      dwhitford@vaultmeridan-example.com
    </li>
  </ul>
  <div class="front-band">4120 Harbor Crest Rd Suite 210 Linden, Maryland 21099</div>
</section>

<section class="card card-back" aria-label="Business card back">
  <div class="back-map" role="img" aria-label="Faint dotted world map background"></div>
  <div class="back-brand"><span class="brand-mark"></span>VaultMeridan</div>
  <ul class="offerings">
    <li>Red/Blue Team<span class="sep">|</span>Secure Virtual Computing<span class="sep">|</span>Data Center Consolidation</li>
    <li>Classified Cross Domain Solutions<span class="sep">|</span>Secure Cloud &amp; Open Stack Solutions</li>
    <li>Network Attack Penetration &amp; Defense<span class="sep">|</span>Data Encrypting/Privacy<span class="sep">|</span>Secure Wireless Solutions</li>
    <li>Certification &amp; Accreditation<span class="sep">|</span>Security Subject Matter Experts</li>
    <li>Executive Security Strategy Coaching<span class="sep">|</span>Foreign/Counter Intelligence Data Security</li>
    <li>Security Training, Assessment &amp; Integration</li>
  </ul>
  <div class="back-web"><span class="rule"></span>www.vaultmeridan-example.com<span class="rule"></span></div>
</section>

</body>
</html>
```